Tressvane hair oil bottle & packaging (Instagrammable)

I'm a blogger/social media influencer and I'm launching my own hair oil that I created myself. The hair oil is something I've used fora a long time and it makes your hair grow like there's no tomorrow!

I'm looking for a feminine and minimalistic bottle for the hair oil and also a nice packaging for the bottle. Please have a look at my Instagram account (@minaveltroo), I'd love if the product design and color scheme would be inspired by my Instagram feed. I'm looking for a design that would look very 'Instagrammable'

Product name: Tressvane
Bottle size: 100ml

Thank you xx

Target Market(s)

Females

Requirements
Must have
• According to the law this has to be marked on the packaging and on the bottle:
• Amount: 100ml
• Marked on the packaging:
• Ingredients: Burdock root oil, Grapeseed oil, Organic castor oil (maybe somehow draw attention to the fact that it's organic when designing the bottle & packaging), peppermint oil, Lavender oil, Cedarwood oil, Rosemary oil
Nice to have
• I added some photos of Ai Wenna packaging - I absolutely love it! The colour is exactly what I have in mind (also if you check my Instagram it's kind of my 'feed colour' - I'd be happy if the packaging would look something like that. The Ai Wenna packaging is exactly what I meant by 'Instagrammable'.
• Also - if we go for something like this, we could write Glow up! on the inside (so you see that when opening the packaging) or feel free to come up with something yourself, just bear in mind it's a hair oil that promotes hair growth

```html
<!DOCTYPE html>
<html lang="en">
<head>
<meta charset="utf-8">
<title>Tressvane — Hair Oil Box Dieline</title>
<link href="https://fonts.googleapis.com/css2?family=Josefin+Sans:wght@400&family=Playfair+Display:wght@700&display=swap" rel="stylesheet">
<style>
  :root {
    --paper: #ffffff;
    --blush: #efd5c5;
    --blush-wave-a: #f3dccf;
    --blush-wave-b: #ecccb9;
    --blush-light: #f8ebe3;
    --mist: #d8eaec;
    --copper: #c07a55;
    --copper-deep: #a9603d;
    --white: #ffffff;
  }
  html, body {
    margin: 0;
    width: 1200px;
    height: 1200px;
    overflow: hidden;
    background: var(--paper);
  }
  .canvas {
    position: relative;
    width: 1500px;
    height: 1500px;
    transform: scale(0.8);
    transform-origin: 0 0;
  }
  .panel { position: absolute; }
  .panel--solid { background: var(--blush); }
  .panel--light { background: var(--blush-light); }
  .panel--inside { background: var(--mist); }
  .panel--wave {
    background: linear-gradient(160deg, var(--blush-wave-a) 0%, var(--blush-wave-b) 50%, var(--blush-wave-a) 100%);
  }
  .vertical {
    position: absolute;
    white-space: nowrap;
    transform-origin: 0 0;
  }
  .brand-spine {
    font-family: "Josefin Sans", sans-serif;
    font-size: 22px;
    letter-spacing: 12px;
    color: var(--copper);
    left: 394px;
    top: 272px;
    transform: rotate(90deg);
  }
  .social-handle {
    font-family: "Josefin Sans", sans-serif;
    font-size: 11px;
    letter-spacing: 2px;
    color: var(--white);
    opacity: 0.85;
    left: 1143px;
    top: 318px;
    transform: rotate(90deg);
  }
  .brand-lid {
    font-family: "Josefin Sans", sans-serif;
    font-size: 15px;
    letter-spacing: 7px;
    color: var(--white);
    left: 260px;
    top: 1192px;
    transform: rotate(-90deg);
  }
  .tagline {
    font-family: "Playfair Display", serif;
    font-weight: 700;
    font-size: 76px;
    line-height: 1;
    color: var(--copper);
    left: 346px;
    top: 1274px;
    transform: rotate(-90deg);
  }
</style>
</head>
<body>
<main class="canvas">
  <!-- outer sleeve -->
  <section class="sleeve">
    <div class="panel panel--wave" style="left:724px;top:43px;width:393px;height:133px" role="img" aria-label="Soft blush wave-line pattern"></div>
    <div class="panel panel--solid" style="left:200px;top:176px;width:917px;height:391px"></div>
    <div class="panel panel--wave" style="left:1117px;top:176px;width:132px;height:391px" role="img" aria-label="Soft blush wave-line pattern"></div>
    <div class="panel panel--wave" style="left:724px;top:567px;width:393px;height:133px" role="img" aria-label="Soft blush wave-line pattern"></div>
    <span class="vertical brand-spine">TRESSVANE</span>
    <span class="vertical social-handle">@minaveltroo</span>
  </section>

  <!-- inner tray -->
  <section class="tray">
    <div class="panel panel--wave" style="left:200px;top:932px;width:393px;height:389px" role="img" aria-label="Soft blush wave-line pattern"></div>
    <div class="panel panel--light" style="left:593px;top:932px;width:131px;height:390px"></div>
    <div class="panel panel--light" style="left:724px;top:800px;width:392px;height:132px"></div>
    <div class="panel panel--inside" style="left:724px;top:932px;width:392px;height:390px"></div>
    <div class="panel panel--light" style="left:724px;top:1322px;width:392px;height:131px"></div>
    <div class="panel panel--light" style="left:1116px;top:932px;width:131px;height:390px"></div>
    <span class="vertical brand-lid">TRESSVANE</span>
    <span class="vertical tagline">glow up!</span>
  </section>
</main>
</body>
</html>
```